Business Card and Letterhead for Vantage Psychology

We need a business card design and letterhead to use for our Psychology firm that specializes in psychoeducational assessments and individual therapy. Our motto is Purpose-Driven Assessments, Meaning-Centered Therapy.Our contact information is as follows:
Vantage Psychology
The Marwick Block - 6127-48St.
Box 2716 Olds, AB
T2K 3M8
t 403.555.0148 (VANT)
f 403.555.0172
www.vantagepsychology-example.ca
The business card will be used for two different psychologists so I can supply names nearer to completion. We prefer clean, uncluttered looks.

Target Market(s)

Clients, Educators

Font styles to use
Sans Serif

Colors

Designer to choose colors to be used in the design.

Requirements
Must have
• All relevant contact info, logo, some "white" space.
Nice to have
• It would be nice to see letterhead options that have the logo on the top of the page but also options that have it on the side. I think top of the page is probably our preference.
Should not have
• Too much clutter!

```html
<!DOCTYPE html>
<html lang="en">
<head>
<meta charset="utf-8">
<title>Vantage Psychology – Stationery</title>
<link rel="stylesheet" href="https://fonts.googleapis.com/css2?family=Open+Sans:wght@400;600;700&display=swap">
<style>
:root{
  --bg:#e6e4e1;
  --paper:#ffffff;
  --blue:#4ab6d5;
  --orange:#f3994a;
  --ink:#3a3a3a;
  --rule:#2b2b2b;
}
*{box-sizing:border-box;margin:0;padding:0}
html,body{width:1200px;height:800px;overflow:hidden;background:var(--bg);font-family:"Open Sans",Arial,sans-serif;color:var(--ink)}
.canvas{position:relative;width:1200px;height:800px}

/* brand name set as plain text */
.brand{position:absolute;left:0;right:0;text-align:center;color:var(--blue);font-weight:600;white-space:nowrap;line-height:1}

/* letterhead */
.letterhead{position:absolute;left:150px;top:30px;width:525px;height:740px;background:var(--paper);box-shadow:0 2px 10px rgba(0,0,0,.12);overflow:hidden}
.letterhead .brand{top:110px;font-size:17px}
.lh-rule{position:absolute;left:70px;right:70px;top:134px;border-top:1.2px solid var(--rule)}
.lh-contact{position:absolute;top:141px;left:0;right:0;text-align:center;font-size:7px;color:var(--ink)}
.lh-contact b{color:var(--blue);font-weight:700;margin-left:6px}
.lh-date{position:absolute;top:231px;right:70px;font-size:8.3px}
.lh-body{position:absolute;top:276px;left:70px;right:66px;font-size:8.1px;line-height:16.7px;color:var(--ink)}
.lh-body p+p{margin-top:16.7px}
.lh-watermark{position:absolute;top:440px;left:0;right:0;text-align:center;font-size:28px;font-weight:600;color:var(--blue);opacity:.13}
.lh-signature{position:absolute;top:544px;left:70px;width:82px;height:20px;background:linear-gradient(90deg,#e9e9e9,#f4f4f4);border-radius:3px}
.lh-signer{position:absolute;top:570px;left:70px;font-size:8px;line-height:10px}
.lh-signer strong{font-weight:700;display:block}
.lh-web{position:absolute;top:683px;left:70px;font-size:7.6px;font-weight:700;letter-spacing:.12em;color:var(--orange)}
.wave{position:absolute;left:0;bottom:0;width:100%}

/* business cards */
.card{position:absolute;left:770px;width:320px;height:195px;background:var(--paper);box-shadow:0 2px 8px rgba(0,0,0,.12);overflow:hidden}
.card-front{top:110px}
.card-back{top:355px}
.card-front .brand{top:72px;left:auto;right:20px;text-align:right;font-size:11px}
.person{position:absolute;top:89px;left:18px}
.person-name{font-size:8px;font-weight:600;color:var(--blue);text-transform:uppercase}
.person-name span{color:var(--orange)}
.person-title{font-size:5.5px;font-weight:600;color:var(--ink)}
.phones{position:absolute;top:123px;left:18px;font-size:5.5px;line-height:10.5px;list-style:none}
.phones li{display:flex;align-items:center;gap:5px}
.phones svg{width:6px;height:6px;fill:var(--blue)}
.address{position:absolute;top:152px;left:18px;font-size:5.5px;line-height:8.5px}
.address-block{color:var(--orange);font-weight:700;text-transform:uppercase}
.address-line{font-weight:700}
.card-back .brand{top:112px;font-size:16px}
.card-web{position:absolute;top:174px;left:0;right:0;text-align:center;font-size:6px;font-weight:700;letter-spacing:.1em}
</style>
</head>
<body>
<main class="canvas">

  <article class="letterhead">
    <div class="brand">Vantage Psychology</div>
    <div class="lh-rule"></div>
    <p class="lh-contact"><b>A:</b> 1450 W. Harlow Ave. Suite 310 <b>E:</b> info@vantagepsychology-example.ca <b>P:</b> 844-555-0190</p>
    <p class="lh-date">Date, 10 September, 2019</p>
    <div class="lh-watermark" aria-hidden="true">Vantage Psychology</div>
    <div class="lh-body">
      <p>This is a sample letter that has been placed to demonstrate typing format (Your Company). letterhead design. When positioned properly, it will serve to work in harmony with all other elements letterhead. This letterhead design is meant to project an image</p>
      <p>This letterhead design is meant to project an image of professionalism reliability. By using simple alignment we have created a very spacious feeling. The simplicity suggests strength, the spaciousness contributes to the aesthetics of the layout. These basic qualities along with the (Your Company)</p>
      <p>look and helps reinforce the (Your Company) brand. letterhead design is meant to project an image of design. When positioned properly, it will serve to work in harmony all the other elements letterhead. professionalism and reliability.</p>
      <p>This letterhead design is based on the (Form of your logo) form (Your Company) letterhead stationery we have created a very spacious feeling. The simplicity suggests strength, spaciousness contributes to part of the (Form of your logo).</p>
    </div>
    <div class="lh-signature" role="img" aria-label="Handwritten signature of Alan Prewitt"></div>
    <p class="lh-signer"><strong>Alan Prewitt</strong>Manager</p>
    <p class="lh-web">www.vantagepsychology-example.ca</p>
    <svg class="wave" viewBox="0 0 525 70" height="70" preserveAspectRatio="none" aria-hidden="true">
      <path d="M70 58 C250 52 430 40 525 18 L525 34 C430 52 250 58 70 58Z" fill="var(--orange)"/>
      <path d="M0 50 C200 50 420 46 525 36 L525 70 L0 70Z" fill="var(--blue)"/>
    </svg>
  </article>

  <section class="card card-front">
    <div class="brand">Vantage Psychology</div>
    <div class="person">
      <p class="person-name">Dana <span>Whitcombe</span></p>
      <p class="person-title">Owner / Founder</p>
    </div>
    <ul class="phones">
      <li><svg viewBox="0 0 10 10"><path d="M2 1l2 2-1 1.2c.6 1.2 1.6 2.2 2.8 2.8L7 6l2 2-1.3 1.3C4.5 9 1 5.5.7 2.3z"/></svg>403.555.0148 (VANT)</li>
      <li><svg viewBox="0 0 10 10"><path d="M2 1l2 2-1 1.2c.6 1.2 1.6 2.2 2.8 2.8L7 6l2 2-1.3 1.3C4.5 9 1 5.5.7 2.3z"/></svg>403.555.0172</li>
    </ul>
    <div class="address">
      <p class="address-block">The Marwick Block</p>
      <p class="address-line">6127-48St. Box 2716 Olds, AB T2K 3M8</p>
    </div>
    <svg class="wave" viewBox="0 0 320 50" height="50" preserveAspectRatio="none" aria-hidden="true">
      <path d="M0 36 C120 32 250 22 320 0 L320 50 L0 50Z" fill="var(--orange)"/>
      <path d="M0 38 C120 35 250 28 320 14 L320 50 L0 50Z" fill="var(--paper)"/>
      <path d="M0 40 C120 38 250 32 320 18 L320 50 L0 50Z" fill="var(--blue)"/>
    </svg>
  </section>

  <section class="card card-back">
    <div class="brand">Vantage Psychology</div>
    <p class="card-web">www.vantagepsychology-example.ca</p>
  </section>

</main>
</body>
</html>
```